Graphic background for 10 Pull Up Banners

To produce a graphic background for a 100 cm wide by 200 cm high Pull-Up Display banner containing a Buddhist text in three languages: Tibetan, Mandarin and English. Please refer to uploaded file "Elements of Pull Up Banner". The design should be simple (not drawing attention away from the text). This design should then be varied for or extended to the next banner and so on until the 10th banner. When the banners are lined up, they should form a single design that is 1000 cm wide by 200 cm high.
An alternative way to look at the project is to produce a graphic background of 1000 cm width by 200 cm height that is then splitted into ten separate 100 cm wide by 200 cm high graphic to be used as background for 10 Buddhist texts (text 1, 2, 3, 4, 5, 6, 7, 8, 9a, 9b) on 10 Pull-Up Display Banners, the text in each banner being in the three languages mentioned earlier.
In either perspective, the design should be simple and not draw attention away from the texts. See uploaded PDF file "Examples.pdf"
For attendees at a Buddhist Event.

```html
<!DOCTYPE html>
<html lang="en">
<head>
<meta charset="utf-8">
<title>Desire &amp; Attachment – Banner Series</title>
<link rel="stylesheet" href="https://fonts.googleapis.com/css2?family=Noto+Sans+SC:wght@400;500&family=Noto+Serif+Tibetan:wght@400;500&family=Open+Sans:wght@400;600&display=swap">
<style>
  :root {
    --deep-red: #7a1e0c;
    --gold: #e6bf78;
    --cream: #fff7ea;
    --medallion: #f6ece4;
    --medallion-mark: #c98a8a;
  }
  * { box-sizing: border-box; margin: 0; padding: 0; }
  html, body { width: 1200px; height: 599px; overflow: hidden; background: var(--deep-red); }
  .canvas { position: relative; width: 1200px; height: 599px; overflow: hidden; }
  .scenery {
    position: absolute; inset: 0;
    background:
      radial-gradient(ellipse 60% 45% at 70% 35%, rgba(255,170,80,.45), transparent 70%),
      linear-gradient(180deg, rgba(0,0,0,0) 55%, rgba(110,30,10,.55) 100%),
      linear-gradient(90deg, #6e1d0e 0%, #9c2a10 18%, #d8471a 45%, #e8621e 70%, #ec7a2a 100%);
  }
  .border-band {
    position: absolute; left: 0; width: 1200px; height: 26px;
    border-top: 2px solid var(--gold); border-bottom: 2px solid var(--gold);
    background: linear-gradient(180deg, rgba(230,191,120,.25), rgba(185,138,62,.15));
  }
  .border-band.top { top: 14px; }
  .border-band.bottom { top: 553px; }
  .panel {
    position: absolute; top: 0; width: 300px; height: 599px;
    border-left: 1px solid rgba(255,230,200,.25);
    color: var(--cream); text-align: center;
  }
  .panel:nth-child(3) { left: 0; border-left: none; }
  .panel:nth-child(4) { left: 300px; }
  .panel:nth-child(5) { left: 600px; }
  .panel:nth-child(6) { left: 900px; }
  .medallion {
    position: absolute; left: 120px; top: 4px; width: 60px; height: 60px; border-radius: 50%;
    background: radial-gradient(circle, var(--medallion) 55%, #e9d8cc 100%);
    border: 2px solid var(--gold);
  }
  .medallion::after {
    content: ""; position: absolute; left: 16px; top: 12px; width: 24px; height: 32px;
    border-radius: 40% 40% 30% 30%; background: var(--medallion-mark); opacity: .5;
  }
  .title {
    position: absolute; top: 64px; left: 0; width: 300px; line-height: 14px;
    font-family: "Noto Sans SC", "Open Sans", sans-serif; font-size: 8.5px; font-weight: 500;
  }
  .title .en { font-family: "Open Sans", sans-serif; }
  .rule { position: absolute; left: 55px; width: 190px; height: 1px; background: rgba(255,240,220,.8); }
  .divider { position: absolute; left: 55px; width: 190px; height: 1px; background: rgba(255,240,220,.8); }
  .divider::after {
    content: ""; position: absolute; left: 85px; top: -3px; width: 20px; height: 7px;
    border-radius: 50%; border: 1px solid rgba(255,240,220,.9);
  }
  .tibetan {
    position: absolute; left: 0; width: 300px;
    font-family: "Noto Serif Tibetan", serif; font-size: 13.5px; line-height: 21px; white-space: nowrap;
  }
  .chinese {
    position: absolute; left: 0; width: 300px;
    font-family: "Noto Sans SC", sans-serif; font-size: 12px; line-height: 17.3px;
  }
  .english {
    position: absolute; left: 0; width: 300px;
    font-family: "Open Sans", sans-serif; font-weight: 600; font-size: 8.6px; line-height: 23px;
  }
  .index .title { font-size: 12px; font-weight: 600; top: 65px; }
  .index .tibetan { font-size: 7.2px; line-height: 12.4px; }
  .index .chinese { font-size: 7.4px; line-height: 11.4px; }
  .index .notes {
    position: absolute; left: 0; width: 300px;
    font-family: "Noto Sans SC", sans-serif; font-size: 4.6px; line-height: 12px;
  }
  .index .english { font-size: 5.6px; line-height: 10.8px; }
</style>
</head>
<body>
<div class="canvas">
  <div class="scenery" role="img" aria-label="Warm orange sky over a hillside palace with a faint seated statue on the right"></div>
  <div class="border-band top" role="img" aria-label="Golden knotwork border"></div>

  <section class="panel index">
    <div class="medallion" role="img" aria-label="Round emblem with a seated deity illustration"></div>
    <h1 class="title">十个误解 &nbsp;&nbsp;- &nbsp;&nbsp;<span class="en">Ten Mistaking</span></h1>
    <div class="rule" style="top:86px"></div>
    <div class="tibetan" style="top:94px">
      དད་པ་དང་འདོད་པ་ལ་འཁྲུལ་ཉེན།།<br>
      བྱམས་སྙིང་རྗེ་དང་ཆགས་པ་ལ་འཁྲུལ་ཉེན།།<br>
      ཤེས་བྱའི་གཤིས་སྟོང་དང་བློས་བྱས་སྟོང་པ་ལ་འཁྲུལ་ཉེན།།<br>
      ཆོས་དབྱིངས་དང་ཆད་ལྟ་ལ་འཁྲུལ་ཉེན།།<br>
      ཉམས་མྱོང་དང་རྟོགས་པ་ལ་འཁྲུལ་ཉེན།།<br>
      བཙུན་པ་དང་རྫུ་འཕྲུལ་ལ་འཁྲུལ་ཉེན།།<br>
      འཁྲུལ་ཞིག་པ་དང་བདུད་ཞུགས་ལ་འཁྲུལ་ཉེན།།<br>
      གྲུབ་ཐོབ་དང་མགོ་སྐོར་བ་ལ་འཁྲུལ་ཉེན།།<br>
      གཞན་དོན་དང་རང་དོན་ལ་འཁྲུལ་ཉེན།།<br>
      ཐབས་མཁས་དང་གཡོ་སྒྱུ་ལ་འཁྲུལ་ཉེན།།
    </div>
    <div class="divider" style="top:232px"></div>
    <div class="chinese" style="top:248px">
      信心与爱欲可能混淆，<br>
      慈悲与贪执可能混淆，<br>
      所知¹本空与思维造作空性可能混淆，<br>
      法界与断见²可能混淆，<br>
      觉受与证悟可能混淆，<br>
      尊者与神棍可能混淆，<br>
      破惑与著魔可能混淆，<br>
      成就者与骗子可能混淆，<br>
      利他与自利可能混淆，<br>
      方便善巧与谄媚哄骗可能混淆。
    </div>
    <div class="notes" style="top:373px">
      1．所知：可以认识的外境。<br>
      2．断见：否定因果、前生、后世等说法的见解。
    </div>
    <div class="divider" style="top:411px"></div>
    <div class="english" style="top:425px">
      Desire can be mistaken for faith or devotion.<br>
      Attachment can be mistaken for love and compassion.<br>
      Conceptual emptiness can be mistaken for the emptiness of the nature of phenomena.<br>
      Nihilism can be mistaken for the dharmadhatu.<br>
      A meditative experience can be mistaken for realization.<br>
      Outer religious practices can be mistaken for inner development of good qualities.<br>
      A person in the grip of a demon can be mistaken for a person who has destroyed his own delusions.<br>
      A charlatan can be mistaken for a siddha.<br>
      An act to benefit yourself can be mistaken for an act to benefit others.<br>
      Deviousness can be mistaken for skilful means.
    </div>
  </section>

  <section class="panel verse">
    <div class="medallion" role="img" aria-label="Round emblem with a seated deity illustration"></div>
    <h2 class="title">欲与爱 &nbsp;&nbsp;- &nbsp;&nbsp;<span class="en">Desire &amp; Attachment</span></h2>
    <div class="rule" style="top:92px"></div>
    <div class="tibetan" style="top:103px">
      འདོད་པ་མེད་ན་རང་དོན་མི་འགྲུབ་ཀྱང་།།<br>
      འདོད་པ་ཡོད་ཚད་ཆགས་པ་མི་ཡིན་པས།།<br>
      འདོད་དང་ཆགས་པའི་ཁྱད་པར་མ་ཤེས་པར།།<br>
      འདོད་ཆགས་ལམ་དུ་ཁྱེར་བ་བླུན་པར་རེས།།
    </div>
    <div class="divider" style="top:206px"></div>
    <div class="chinese" style="top:228px">
      若无意欲则不成自利，<br>
      然有意欲非为执着故，<br>
      不知意欲执着差别即，<br>
      贪执说所当取确荒唐。
    </div>
    <div class="divider" style="top:326px"></div>
    <div class="english" style="top:346px">
      If you have no desire, your goal cannot be achieved.<br>
      Since not all desire is attachment,<br>
      not knowing how to differentiate desire from attachment,<br>
      to talk about bringing passion into the path is absurd.
    </div>
  </section>

  <section class="panel verse">
    <div class="medallion" role="img" aria-label="Round emblem with a seated deity illustration"></div>
    <h2 class="title">欲与爱 &nbsp;&nbsp;- &nbsp;&nbsp;<span class="en">Desire &amp; Attachment</span></h2>
    <div class="rule" style="top:92px"></div>
    <div class="tibetan" style="top:103px">
      འདོད་པ་མེད་ན་རང་དོན་མི་འགྲུབ་ཀྱང་།།<br>
      འདོད་པ་ཡོད་ཚད་ཆགས་པ་མི་ཡིན་པས།།<br>
      འདོད་དང་ཆགས་པའི་ཁྱད་པར་མ་ཤེས་པར།།<br>
      འདོད་ཆགས་ལམ་དུ་ཁྱེར་བ་བླུན་པར་རེས།།
    </div>
    <div class="divider" style="top:206px"></div>
    <div class="chinese" style="top:228px">
      若无意欲则不成自利，<br>
      然有意欲非为执着故，<br>
      不知意欲执着差别即，<br>
      贪执说所当取确荒唐。
    </div>
    <div class="divider" style="top:326px"></div>
    <div class="english" style="top:346px">
      If you have no desire, your goal cannot be achieved.<br>
      Since not all desire is attachment,<br>
      not knowing how to differentiate desire from attachment,<br>
      to talk about bringing passion into the path is absurd.
    </div>
  </section>

  <section class="panel verse">
    <div class="medallion" role="img" aria-label="Round emblem with a seated deity illustration"></div>
    <h2 class="title">欲与爱 &nbsp;&nbsp;- &nbsp;&nbsp;<span class="en">Desire &amp; Attachment</span></h2>
    <div class="rule" style="top:92px"></div>
    <div class="tibetan" style="top:103px">
      འདོད་པ་མེད་ན་རང་དོན་མི་འགྲུབ་ཀྱང་།།<br>
      འདོད་པ་ཡོད་ཚད་ཆགས་པ་མི་ཡིན་པས།།<br>
      འདོད་དང་ཆགས་པའི་ཁྱད་པར་མ་ཤེས་པར།།<br>
      འདོད་ཆགས་ལམ་དུ་ཁྱེར་བ་བླུན་པར་རེས།།
    </div>
    <div class="divider" style="top:206px"></div>
    <div class="chinese" style="top:228px">
      若无意欲则不成自利，<br>
      然有意欲非为执着故，<br>
      不知意欲执着差别即，<br>
      贪执说所当取确荒唐。
    </div>
    <div class="divider" style="top:326px"></div>
    <div class="english" style="top:346px">
      If you have no desire, your goal cannot be achieved.<br>
      Since not all desire is attachment,<br>
      not knowing how to differentiate desire from attachment,<br>
      to talk about bringing passion into the path is absurd.
    </div>
  </section>

  <div class="border-band bottom" role="img" aria-label="Golden knotwork border"></div>
</div>
</body>
</html>
```